Linked In Profile Banner Needed

I am in need of a Linked In Banner photo for my profile. The dimensions are 1584 x 396 pixels and the bottom left is where Linked In places my photo over so be aware of that. I attached an example for your reference.

I have also attached my logo and business card so you can keep the same color & style conistant.

Also add the following text:

"Preserve capital with a tax advantaged lease for equipment, vehicles, software and more! $5,000 - $50m"

You can also look at our website here:
www.HarlowfieldFundingCo.com

```html
<!DOCTYPE html>
<html lang="en">
<head>
<meta charset="utf-8">
<title>Harlowfield Funding Co – LinkedIn Banner</title>
<link href="https://fonts.googleapis.com/css2?family=Lato:wght@400&family=Alegreya+Sans:ital,wght@1,500&display=swap" rel="stylesheet">
<style>
  :root {
    --page: #ffffff;
    --banner: #383447;
    --wordmark: #ffffff;
    --accent-square: #5a86c4;
    --rule: #4a5487;
    --tagline: #6ec3e6;
  }
  html, body {
    margin: 0;
    padding: 0;
    width: 1200px;
    height: 434px;
    overflow: hidden;
    background: var(--page);
  }
  .canvas {
    position: relative;
    width: 1200px;
    height: 434px;
    background: var(--page);
  }
  .banner {
    position: absolute;
    left: 48px;
    top: 121px;
    width: 1112px;
    height: 192px;
    background: var(--banner);
  }
  .brand {
    position: absolute;
    left: 556px;
    top: 24px;
    transform: translateX(-50%);
    display: flex;
    align-items: center;
    gap: 18px;
    white-space: nowrap;
  }
  .brand-square {
    width: 52px;
    height: 52px;
    background: var(--accent-square);
  }
  .brand-name {
    font-family: "Lato", sans-serif;
    font-weight: 400;
    font-size: 32px;
    letter-spacing: 1px;
    color: var(--wordmark);
    text-transform: uppercase;
  }
  .divider {
    position: absolute;
    left: 259px;
    top: 118px;
    width: 594px;
    height: 1px;
    background: var(--rule);
  }
  .tagline {
    position: absolute;
    left: 584px;
    top: 136px;
    transform: translateX(-50%);
    margin: 0;
    width: 460px;
    text-align: center;
    font-family: "Alegreya Sans", sans-serif;
    font-style: italic;
    font-weight: 500;
    font-size: 16px;
    line-height: 19px;
    color: var(--tagline);
  }
</style>
</head>
<body>
  <div class="canvas">
    <section class="banner">
      <div class="brand">
        <div class="brand-square"></div>
        <span class="brand-name">Harlowfield Funding Co</span>
      </div>
      <div class="divider"></div>
      <p class="tagline">Preserve capital with a tax advantaged lease for equipment,<br>vehicles, software and more! $5,000 - $50m</p>
    </section>
  </div>
</body>
</html>
```